Harlow Vance Law Stationary - logo provided

I need Stationary designed for my Law Firm named Harlow Vance Law.

I have attached the firm's logo and would like that color and logos incorporated into the stationary. I need the stationary to look clean, simple and professional.

I need letterheads, envelopes and business cards designed. I would also like a letterhead version for 5.5 x 8..5 paper size (for handout printing)

Industry/Entity Type

Legal

```html
<!DOCTYPE html>
<html lang="en">
<head>
<meta charset="UTF-8">
<title>Harlow Vance Law – Letterhead 5.5 x 8.5</title>
<link href="https://fonts.googleapis.com/css2?family=Cinzel:wght@500&family=Open+Sans:wght@600&display=swap" rel="stylesheet">
<style>
  :root {
    --maroon: #7a1f1a;
    --gold: #c9a25e;
    --paper: #ffffff;
    --label: #333333;
  }
  * { margin: 0; padding: 0; box-sizing: border-box; }
  html, body { width: 739px; height: 1200px; overflow: hidden; background: var(--paper); }
  .letterhead { position: relative; width: 739px; height: 1200px; background: var(--paper); }
  .corner { position: absolute; display: block; }
  .corner--top-left { left: 0; top: 0; }
  .corner--bottom-right { right: 0; bottom: 0; }
  .mark-square { position: absolute; border: 3px solid var(--gold); }
  .mark-square--top { right: 40px; top: 32px; width: 36px; height: 36px; }
  .mark-square--foot { left: 18px; top: 1072px; width: 34px; height: 34px; }
  .footer-rule { position: absolute; left: 60px; top: 1088px; width: 540px; height: 3px; background: var(--gold); }
  .brand {
    position: absolute; left: 0; right: 0; top: 550px;
    display: flex; align-items: center; justify-content: center; gap: 22px;
  }
  .brand__square { width: 66px; height: 66px; border: 4px solid var(--gold); }
  .brand__name {
    font-family: "Cinzel", serif; font-weight: 500; color: var(--maroon);
    font-size: 40px; letter-spacing: 2px; line-height: 1;
  }
  .size-label {
    position: absolute; right: 10px; bottom: 6px;
    font-family: "Open Sans", sans-serif; font-weight: 600; font-size: 13px; color: var(--label);
  }
</style>
</head>
<body>
<main class="letterhead">
  <svg class="corner corner--top-left" width="290" height="290" viewBox="0 0 290 290" aria-hidden="true">
    <path d="M0 0 H280 Q140 60 0 280 Z" fill="var(--gold)"/>
    <path d="M300 -6 Q150 60 -6 300" fill="none" stroke="var(--paper)" stroke-width="14"/>
    <path d="M300 -6 Q150 60 -6 300" fill="none" stroke="var(--maroon)" stroke-width="8" stroke-dasharray="60 14"/>
  </svg>

  <div class="mark-square mark-square--top"></div>

  <div class="brand">
    <div class="brand__square"></div>
    <div class="brand__name">Harlow Vance Law</div>
  </div>

  <div class="mark-square mark-square--foot"></div>
  <div class="footer-rule"></div>

  <svg class="corner corner--bottom-right" width="300" height="300" viewBox="0 0 300 300" aria-hidden="true">
    <path d="M300 300 H20 Q160 240 300 20 Z" fill="var(--gold)"/>
    <path d="M0 306 Q150 240 306 0" fill="none" stroke="var(--paper)" stroke-width="14"/>
    <path d="M0 306 Q150 240 306 0" fill="none" stroke="var(--maroon)" stroke-width="8" stroke-dasharray="60 14"/>
  </svg>

  <div class="size-label">Letter Head 5.5 X 8.5</div>
</main>
</body>
</html>
```